Magazine Template for National Charity

We need a magazine design for an Australian youth charity called Beats Opening Local Doors (BOLD). We engage young people through street culture music, dance and mentoring programs, and help them to turn their lives around. Our charity's vision is to see every young person have someone who believes in them and the opportunity to live their potential.

The design should have places for images of our young people during programs(we've only provided a few for you), room for quotes from young people and supporters etc, and each double spread could be a snapshot of a different program.

We will need a design template that will allow us to add all the contents for the magazine, including a contents page, report from our Chairman (1 page), letter from CEO (1 page), and following achievements of our programs including 1. BOLD Camps (2 x double spread, total 4 pages), 2. Riverbend Jams (2 x double spread, total 4 pages) and 3. Mentoring (2 x double spread, total 4 pages). An audited financial report of 4 pages will be copied in after our program reports, and on the back of the magazine, we'll need space for all our supporter logos. I'd also like to include a short story or case-study about young people's transformation on each program page.

We need something that's got a bit of a street edge, to keep our youthful brand, but helps us to highlight our excellence as an innovative and cutting edge charity. The final design should be emotional, eye-catching, reflective of our creative spark, and inspiring. We currently have a brand that uses a fair bit of black & white with highlights of colour, however I dont want this to limit your creativity. We use a font called Octin Spraypaint Free for our logos and program names.

We would like to present our annual report as a magazine so that it is something that people will want to pick up and look at.

Target Market(s)

This is for general public and supporters, however we'd like to use our brand instead of a professional style for this report

Industry/Entity Type

Financial

Requirements
Must have
• See notes in task description - thank you!

We will give you a few images to use as a guide however we'd love to be able to play around with the images once we have a template (we'll add different ones and change pictures around to suit the program pages). We're providing these images so that you can get a feel for our culture and be inspired to put together the template, dont worry if you use the same photos more than once on the different pages to show as an example.
Nice to have
• We already have our charity logo, however we'd love to call this BOLD Mag, BOLD Magazine or Latest BOLDness. We'd like it to replicate a real magazine, with colour and lots of interesting sections for information & stories, rather than a boring traditional annual report template.
Should not have
• We want this magazine to stand out, and we dont want a half-hearted charity design or a polished corporate style magazine.

We want to remain bold and contemporary, and on the commercial side with a street edge - have lots of fun & thank you so much - we're very excited!

```html
<!DOCTYPE html>
<html lang="en">
<head>
<meta charset="utf-8">
<title>BOLD Mag – A Word From Our Chair &amp; CEO</title>
<link rel="stylesheet" href="https://fonts.googleapis.com/css2?family=Open+Sans:wght@400;700&family=Rubik+Dirt&display=swap">
<style>
  :root {
    --ink: #1a1a1a;
    --paper: #ffffff;
    --accent: #f3a632;
    --photo-dark: #141414;
    --photo-mid: #4a4a4a;
    --photo-light: #8c8c8c;
    --muted: #bdbdbd;
  }
  * { box-sizing: border-box; margin: 0; padding: 0; }
  html, body { width: 1200px; height: 855px; overflow: hidden; background: var(--photo-dark); }
  .spread {
    position: relative;
    width: 1200px;
    height: 855px;
    overflow: hidden;
    font-family: "Open Sans", Arial, sans-serif;
    color: var(--ink);
  }
  .spread__photo {
    position: absolute; inset: 0;
    background:
      radial-gradient(ellipse 260px 330px at 420px 300px, var(--photo-light) 0%, var(--photo-mid) 45%, transparent 80%),
      radial-gradient(ellipse 520px 380px at 250px 230px, #6a6a6a 0%, transparent 75%),
      linear-gradient(90deg, #2e2e2e 0%, #3c3c3c 35%, #1c1c1c 60%, var(--photo-dark) 100%);
  }
  .image-credit {
    position: absolute;
    left: 12px; top: 24px;
    writing-mode: vertical-rl;
    transform: rotate(180deg);
    font-size: 7px;
    color: var(--muted);
    letter-spacing: .2px;
  }
  .brand-tab {
    position: absolute;
    top: 0; right: 52px;
    width: 130px; height: 48px;
    background: var(--paper);
    border-radius: 0 0 8px 8px;
    display: flex; align-items: center; gap: 6px;
    padding: 0 8px;
  }
  .brand-tab__mark { width: 9px; height: 9px; background: var(--ink); flex: none; }
  .brand-tab__name {
    font-weight: 700; font-size: 10.5px; line-height: 12px;
    text-transform: uppercase; color: var(--ink);
  }
  .pull-quote {
    position: absolute;
    right: 54px; top: 122px;
    width: 560px;
    text-align: right;
    font-family: "Rubik Dirt", "Open Sans", sans-serif;
    font-size: 56px;
    line-height: 64px;
    color: var(--accent);
    letter-spacing: 2px;
    text-transform: uppercase;
  }
  .badge {
    position: absolute;
    width: 106px; height: 106px;
    border-radius: 50%;
    background: var(--accent);
    display: flex; align-items: center; justify-content: center;
    text-align: center;
    font-family: "Rubik Dirt", "Open Sans", sans-serif;
    color: var(--paper);
    font-size: 15px; line-height: 19px;
    text-transform: uppercase;
    z-index: 2;
  }
  .badge--chair { left: 46px; top: 405px; }
  .badge--ceo { left: 1041px; top: 410px; }
  .letter {
    position: absolute;
    top: 530px; height: 274px;
    background: var(--paper);
    padding: 10px 12px;
    display: grid;
    grid-template-columns: repeat(3, 1fr);
    column-gap: 14px;
    font-size: 9.6px;
    line-height: 13.5px;
  }
  .letter--chair { left: 47px; width: 557px; }
  .letter--ceo { left: 634px; width: 515px; }
  .letter p { margin-bottom: 10px; }
  .letter__sign { font-weight: 700; font-size: 9px; line-height: 12px; }
  .folio {
    position: absolute;
    top: 810px; height: 26px;
    display: flex; align-items: center; gap: 10px;
    font-size: 11px; color: var(--paper);
  }
  .folio__num {
    background: var(--accent); color: var(--paper);
    font-weight: 700; font-size: 15px;
    width: 24px; height: 26px;
    display: flex; align-items: center; justify-content: center;
  }
  .folio--left { left: 47px; }
  .folio--right { right: 52px; }
</style>
</head>
<body>
<main class="spread">
  <div class="spread__photo" role="img" aria-label="Black and white photo of a young performer in a beanie reading lyrics from a sheet of paper"></div>

  <p class="image-credit">Image Credit: BOLD Youth Programs Archive</p>

  <div class="brand-tab">
    <span class="brand-tab__mark"></span>
    <span class="brand-tab__name">Beats Opening Local Doors</span>
  </div>

  <h1 class="pull-quote">“Et dekdef eajaf padjed tofkdu”</h1>

  <div class="badge badge--chair">A word<br>from our<br>chair</div>
  <div class="badge badge--ceo">A word<br>from our<br>CEO</div>

  <article class="letter letter--chair">
    <div class="letter__col">
      <p>Every young person who walked through our doors this year brought a story, a beat and a reason to keep going. Our crews showed up, worked hard and lifted each other higher than ever before.</p>
      <p>Our mentors gave their time, patience and belief, and that belief changed lives in ways we are still counting.</p>
      <p>We grew new programs in regional towns, welcomed fresh partners and kept every session free for the young people who need it most. Thank you to everyone who made this possible.</p>
    </div>
    <div class="letter__col">
      <p>From camps to studio nights, our teams created safe places to create, perform and be heard by people who care.</p>
      <p>Looking ahead, we will keep building pathways into training, work and leadership for every young artist in our community.</p>
      <p>Thank you to our board, staff, volunteers and supporters. Your generosity keeps the music playing and the doors open wide.</p>
    </div>
    <div class="letter__col">
      <p>This magazine celebrates the courage of our young people and the creative spark they bring to every room they enter.</p>
      <p>We are proud of what we achieved together and excited for the year ahead. Let's keep being bold.</p>
      <p class="letter__sign">Professor Alan Whitcombe<br>Chairperson</p>
    </div>
  </article>

  <article class="letter letter--ceo">
    <div class="letter__col">
      <p>Every young person who walked through our doors this year brought a story, a beat and a reason to keep going. Our crews showed up, worked hard and lifted each other higher than ever before.</p>
      <p>Our mentors gave their time, patience and belief, and that belief changed lives in ways we are still counting.</p>
      <p>We grew new programs in regional towns, welcomed fresh partners and kept every session free for the young people who need it most. Thank you to everyone who made this possible.</p>
    </div>
    <div class="letter__col">
      <p>From camps to studio nights, our teams created safe places to create, perform and be heard by people who care.</p>
      <p>Looking ahead, we will keep building pathways into training, work and leadership for every young artist in our community.</p>
      <p>Thank you to our board, staff, volunteers and supporters. Your generosity keeps the music playing and the doors open wide.</p>
    </div>
    <div class="letter__col">
      <p>This magazine celebrates the courage of our young people and the creative spark they bring to every room they enter.</p>
      <p>We are proud of what we achieved together and excited for the year ahead. Let's keep being bold.</p>
      <p class="letter__sign">CEO</p>
    </div>
  </article>

  <footer class="folio folio--left"><span class="folio__num">2</span><span>the power of music</span></footer>
  <footer class="folio folio--right"><span>www.bold.org.au</span><span class="folio__num">3</span></footer>
</main>
</body>
</html>
```